Business Card Design with new logo

Dorian Pelleway 4172
E 118th St Harlow Creek, IL 62999
Cell: 217-555-0193
pellewayrestoration@mailvane.test

Classic Car Restoration Services Buy Sell Trade Consign

Dorian Pelleway 9698
Cell: 217-555-0193

```html
<!DOCTYPE html>
<html lang="en">
<head>
<meta charset="utf-8">
<title>Pelleway Restoration – Business Card</title>
<link href="https://fonts.googleapis.com/css2?family=Roboto:wght@400;700&display=swap" rel="stylesheet">
<style>
  :root {
    --backdrop: #3a3330;
    --card-white: #ffffff;
    --red: #e83e33;
    --red-deep: #b91f27;
    --red-text: #c8202b;
    --navy: #1c2a3a;
    --grey-text: #3b3b3b;
    --rule: #9a9a9a;
  }
  * { box-sizing: border-box; margin: 0; padding: 0; }
  html, body {
    width: 1200px; height: 844px; overflow: hidden;
    background: var(--backdrop);
    font-family: "Roboto", Arial, sans-serif;
  }
  .stage {
    position: relative; width: 1200px; height: 844px;
    display: flex; align-items: center; justify-content: center; gap: 50px;
  }
  .card {
    position: relative; width: 525px; height: 300px;
    box-shadow: 0 12px 30px rgba(0,0,0,.45);
    overflow: hidden;
  }

  /* Front */
  .card-front { background: var(--card-white); }
  .brand {
    position: absolute; top: 42px; right: 36px;
    display: flex; align-items: center; gap: 10px;
  }
  .brand-dot { width: 16px; height: 16px; border-radius: 50%; background: var(--red); }
  .brand-name {
    font-weight: 700; font-size: 21px; color: var(--navy);
    letter-spacing: .5px; text-transform: uppercase;
  }
  .rule { position: absolute; height: 1px; background: var(--rule); }
  .rule-top { top: 100px; left: 250px; right: 30px; }
  .rule-mid { top: 132px; left: 250px; right: 30px; }
  .rule-low { top: 236px; left: 30px; right: 250px; }

  .person { position: absolute; left: 30px; top: 150px; }
  .person-name { font-size: 19px; font-weight: 700; color: var(--navy); text-transform: uppercase; line-height: 1.1; }
  .person-name .first { color: var(--red-text); }
  .person-role { font-size: 13px; color: var(--grey-text); margin-top: 2px; }

  .address { position: absolute; left: 30px; top: 208px; font-size: 13px; color: var(--grey-text); white-space: nowrap; }

  .contact {
    position: absolute; left: 30px; top: 250px;
    font-size: 13px; color: var(--grey-text);
    display: flex; gap: 8px; align-items: center; white-space: nowrap;
  }
  .contact .label { color: var(--red-text); font-weight: 700; }
  .contact .sep { color: var(--rule); }

  /* Back */
  .card-back {
    background: linear-gradient(90deg, var(--red) 0 42%, var(--red-deep) 42% 100%);
    display: flex; align-items: center; justify-content: center;
  }
  .back-name {
    font-weight: 700; font-size: 34px; color: var(--card-white);
    text-transform: uppercase; letter-spacing: 1px; text-align: center; line-height: 1.15;
  }
</style>
</head>
<body>
<main class="stage">
  <section class="card card-front" aria-label="Business card front">
    <div class="brand">
      <span class="brand-dot"></span>
      <span class="brand-name">Pelleway Restoration LLC</span>
    </div>
    <div class="rule rule-top"></div>
    <div class="rule rule-mid"></div>

    <div class="person">
      <p class="person-name"><span class="first">Marcus</span> Tennerly</p>
      <p class="person-role">Managing Director</p>
    </div>

    <p class="address">Dorian Pelleway 4172 E 118th St Harlow Creek, IL 62999</p>
    <div class="rule rule-low"></div>

    <p class="contact">
      <span><span class="label">P:</span> 217-555-0193</span>
      <span class="sep">|</span>
      <span><span class="label">E:</span> pellewayrestoration@mailvane.test</span>
    </p>
  </section>

  <section class="card card-back" aria-label="Business card back">
    <p class="back-name">Pelleway<br>Restoration LLC</p>
  </section>
</main>
</body>
</html>
```